Business Card Design Project

We have a logo design and are now looking for a business card design. We supply pre-construction services to the Wireless Telecommunication Industry in the development of cell phone tower and other antenna supporting infrastructure e.g. buildings. The types of services include Real Estate Leasing, Zoning & Permitting,Surveying and A&E work. I am looking for a card that includes the logo we have selected along with the full company name. Company colors are Blue and Silver. I want something professional and that "pops". Use your imagination with the four sided star portion of the logo - it can be stretched such that it occupies a large portion of the card or kept simple the way it is. I am interested in seeing the design on a white, silver, navy, black or charcoal background or any other color you think works well with the logo. Apart from the logo that includes HRM we also need to see the full company name on the card - Harborline Relay Maintenance, Inc. The design must also show a persons name, title, address, (2) phone numbers, e-mail address and web address www.hrm.example

Target Market(s)

Cell phone carriers e.g. Quellport Mobile, BN&K, Zandex Cell, Ovalo etc.

Industry/Entity Type

Cell Phone

Requirements
Must have
• Logo and
Harborline Relay Maintenance, Inc.

```html
<!DOCTYPE html>
<html lang="en">
<head>
<meta charset="utf-8">
<title>HRM Business Card</title>
<link rel="stylesheet" href="https://fonts.googleapis.com/css2?family=Open+Sans:wght@400;600;700&display=swap">
<style>
  :root {
    --page-bg: #eef0f2;
    --card-white: #ffffff;
    --card-mist: #eceef0;
    --silver-light: #f4f5f6;
    --silver-mid: #c9ccd0;
    --silver-dark: #a8acb1;
    --blue-deep: #1f78c8;
    --blue-bright: #3ea6e6;
    --brand-blue: #2a86d4;
    --title-grey: #8a8f95;
    --company-grey: #7d838a;
    --contact-white: #ffffff;
  }
  * { margin: 0; padding: 0; box-sizing: border-box; }
  html, body {
    width: 1200px;
    height: 900px;
    overflow: hidden;
    background: var(--page-bg);
    font-family: "Open Sans", Arial, sans-serif;
  }
  .stage {
    width: 1200px;
    height: 900px;
    display: flex;
    align-items: center;
    justify-content: center;
  }
  .business-card {
    position: relative;
    width: 900px;
    height: 520px;
    border-radius: 36px;
    overflow: hidden;
    background: linear-gradient(180deg, var(--card-white) 0%, var(--card-mist) 100%);
    box-shadow: 0 18px 40px rgba(30, 50, 80, 0.18);
  }
  .card-top {
    position: absolute;
    inset: 0 0 auto 0;
    height: 236px;
    background: linear-gradient(180deg, var(--card-white) 0%, var(--card-mist) 100%);
  }
  .silver-band {
    position: absolute;
    left: 0; right: 0;
    top: 236px;
    height: 26px;
    background: linear-gradient(180deg, var(--silver-light) 0%, var(--silver-mid) 55%, var(--silver-dark) 100%);
  }
  .blue-panel {
    position: absolute;
    left: 0; right: 0; bottom: 0;
    top: 262px;
    background: linear-gradient(180deg, var(--blue-deep) 0%, var(--blue-bright) 100%);
  }
  .brand {
    position: absolute;
    left: 48px;
    top: 66px;
  }
  .brand-mark {
    display: flex;
    align-items: center;
    gap: 22px;
  }
  .brand-dot {
    width: 64px;
    height: 64px;
    border-radius: 50%;
    background: var(--brand-blue);
  }
  .brand-name {
    font-size: 96px;
    font-weight: 700;
    line-height: 1;
    color: var(--brand-blue);
    letter-spacing: 2px;
  }
  .company-name {
    margin-top: 14px;
    margin-left: 86px;
    font-size: 18px;
    font-weight: 600;
    line-height: 1.2;
    color: var(--company-grey);
    letter-spacing: 0.3px;
    white-space: nowrap;
  }
  .person {
    position: absolute;
    right: 64px;
    top: 40px;
    text-align: right;
  }
  .person-name {
    font-size: 22px;
    font-weight: 600;
    color: var(--brand-blue);
  }
  .person-title {
    font-size: 15px;
    color: var(--title-grey);
    margin-top: 4px;
  }
  .contact-list {
    position: absolute;
    left: 56px;
    top: 290px;
    list-style: none;
  }
  .contact-item {
    display: flex;
    align-items: center;
    gap: 12px;
    height: 40px;
    font-size: 23px;
    color: var(--contact-white);
  }
  .contact-icon {
    width: 22px;
    height: 22px;
    flex: none;
    fill: var(--contact-white);
    opacity: 0.9;
  }
</style>
</head>
<body>
<main class="stage">
  <article class="business-card">
    <div class="card-top"></div>
    <div class="silver-band"></div>
    <div class="blue-panel"></div>

    <div class="brand">
      <div class="brand-mark">
        <span class="brand-dot"></span>
        <span class="brand-name">HRM</span>
      </div>
      <p class="company-name">Harborline Relay Maintenance, Inc.</p>
    </div>

    <div class="person">
      <p class="person-name">Dorian Vale</p>
      <p class="person-title">Manager</p>
    </div>

    <ul class="contact-list">
      <li class="contact-item">
        <svg class="contact-icon" viewBox="0 0 24 24" aria-hidden="true"><path d="M6.6 10.8a15.1 15.1 0 0 0 6.6 6.6l2.2-2.2c.3-.3.7-.4 1-.2 1.1.4 2.3.6 3.6.6.6 0 1 .4 1 1V20c0 .6-.4 1-1 1A17 17 0 0 1 3 4c0-.6.4-1 1-1h3.5c.6 0 1 .4 1 1 0 1.3.2 2.5.6 3.6.1.3 0 .7-.2 1z"/></svg>
        <span>555.014.2290</span>
      </li>
      <li class="contact-item">
        <svg class="contact-icon" viewBox="0 0 24 24" aria-hidden="true"><path d="M6.6 10.8a15.1 15.1 0 0 0 6.6 6.6l2.2-2.2c.3-.3.7-.4 1-.2 1.1.4 2.3.6 3.6.6.6 0 1 .4 1 1V20c0 .6-.4 1-1 1A17 17 0 0 1 3 4c0-.6.4-1 1-1h3.5c.6 0 1 .4 1 1 0 1.3.2 2.5.6 3.6.1.3 0 .7-.2 1z"/></svg>
        <span>555.017.6634</span>
      </li>
      <li class="contact-item">
        <svg class="contact-icon" viewBox="0 0 24 24" aria-hidden="true"><path d="M2 6a2 2 0 0 1 2-2h16a2 2 0 0 1 2 2v12a2 2 0 0 1-2 2H4a2 2 0 0 1-2-2zm2 .5V7l8 5 8-5v-.5z"/></svg>
        <span>dorian@mailvale.example</span>
      </li>
      <li class="contact-item">
        <svg class="contact-icon" viewBox="0 0 24 24" aria-hidden="true"><path d="M12 3 2 12h3v8h5v-5h4v5h5v-8h3z"/></svg>
        <span>4820 Linden Crest, Marlow, TX 70000</span>
      </li>
      <li class="contact-item">
        <svg class="contact-icon" viewBox="0 0 24 24" aria-hidden="true"><path d="M12 2a10 10 0 1 0 0 20 10 10 0 0 0 0-20zm6.9 9h-3c-.1-2.3-.6-4.4-1.4-6A8 8 0 0 1 18.9 11zM12 4c.9 1.2 1.8 3.6 1.9 7h-3.8c.1-3.4 1-5.8 1.9-7zM9.5 5c-.8 1.6-1.3 3.7-1.4 6h-3A8 8 0 0 1 9.5 5zM5.1 13h3c.1 2.3.6 4.4 1.4 6A8 8 0 0 1 5.1 13zm6.9 7c-.9-1.2-1.8-3.6-1.9-7h3.8c-.1 3.4-1 5.8-1.9 7zm2.5-1c.8-1.6 1.3-3.7 1.4-6h3a8 8 0 0 1-4.4 6z"/></svg>
        <span>www.hrm.example</span>
      </li>
    </ul>
  </article>
</main>
</body>
</html>
```